National hospice pharmacy network needs a powerpoint design

We need a power point design for a new company that is creating a network of independent pharmacies to provide medication delivery to hospice patients in their area. We will be providing them with logistics to build a delivery system, software to increase efficiency and the marketing to hospice agencies. The pharmacies will benefit with increasing their patient care, increasing their efficiency and increasing their profits.

Pharmacy

```html
<!DOCTYPE html>
<html lang="en">
<head>
<meta charset="utf-8">
<title>ReachMeds – Pharmacy Network Deck</title>
<link href="https://fonts.googleapis.com/css2?family=Nunito:wght@800;900&family=Carlito:wght@400;700&display=swap" rel="stylesheet">
<style>
  :root {
    --stage: #000000;
    --slide-light: #f4f4f2;
    --slide-grey: #e8e8e8;
    --band-grey: #b4b4b4;
    --brand-blue: #2c5ba6;
    --title-blue: #2a4e8e;
    --brand-green: #3cb54a;
    --bullet-green: #1fb04b;
    --body-ink: #1a1a1a;
  }
  * { margin: 0; padding: 0; box-sizing: border-box; }
  html, body { width: 960px; height: 1200px; overflow: hidden; background: var(--stage); }
  .canvas { position: relative; width: 960px; height: 1200px; background: var(--stage); }

  .slide { position: absolute; left: 102px; width: 768px; height: 576px; overflow: hidden; }
  .slide--cover { top: 18px; background: var(--slide-light); }
  .slide--content { top: 606px; background: var(--slide-grey); }

  .brand-name {
    position: absolute; left: 0; right: 0; top: 140px; text-align: center;
    font-family: "Nunito", sans-serif; font-weight: 800; font-size: 112px;
    line-height: 1; letter-spacing: -3px; color: var(--brand-blue);
  }
  .cover-rule { position: absolute; left: 136px; top: 319px; width: 548px; height: 4px; background: var(--brand-blue); }
  .cover-dot { position: absolute; left: 110px; top: 328px; width: 140px; height: 140px; border-radius: 50%; background: var(--brand-green); }
  .tagline {
    position: absolute; left: 160px; top: 382px;
    font-family: "Nunito", sans-serif; font-weight: 900; font-size: 32px;
    color: var(--title-blue); text-shadow: 1px 1px 2px rgba(0,0,0,.35);
  }

  .title-band { position: absolute; left: 0; top: 28px; width: 100%; height: 62px; background: var(--band-grey); }
  .slide-title {
    position: absolute; left: 22px; top: 5px;
    font-family: "Nunito", sans-serif; font-weight: 900; font-size: 42px; line-height: 1.2;
    color: var(--title-blue); text-shadow: 1px 1px 2px rgba(0,0,0,.3);
  }
  .band-brand {
    position: absolute; right: 16px; top: 13px;
    font-family: "Nunito", sans-serif; font-weight: 800; font-size: 30px; line-height: 1.2;
    letter-spacing: -1px; color: var(--brand-blue);
  }

  .point, .detail { position: absolute; font-family: "Carlito", sans-serif; line-height: 1; white-space: nowrap; }
  .point { left: 76px; font-size: 26px; font-weight: 700; color: var(--bullet-green); }
  .point::before { content: "•"; position: absolute; left: -26px; font-size: 20px; top: 3px; }
  .detail { left: 108px; font-size: 24px; color: var(--body-ink); }
  .detail--lead::before { content: "–"; position: absolute; left: -24px; }
</style>
</head>
<body>
<div class="canvas">
  <section class="slide slide--cover">
    <div class="brand-name">ReachMeds</div>
    <div class="cover-rule"></div>
    <div class="cover-dot"></div>
    <div class="tagline">Helping your pharmacy expand</div>
  </section>

  <section class="slide slide--content">
    <div class="title-band">
      <h1 class="slide-title">Increased Efficiencies</h1>
      <div class="band-brand">ReachMeds</div>
    </div>

    <div class="point" style="top:138px">No data entry</div>
    <div class="detail detail--lead" style="top:182px">Software that seamlessly communicates between</div>
    <div class="detail" style="top:218px">prescribers and your pharmacy</div>
    <div class="detail detail--lead" style="top:261px">Essentially the hospice&nbsp; does all the data entry</div>

    <div class="point" style="top:304px">No phone calls</div>
    <div class="detail detail--lead" style="top:347px">All scripts new and refill done electronically</div>
    <div class="detail detail--lead" style="top:390px">Clinical consultation done by contracted</div>
    <div class="detail" style="top:426px">pharmacists</div>

    <div class="point" style="top:469px">No third party billing</div>
    <div class="detail detail--lead" style="top:512px">Billing and Medicare reporting done for you</div>
  </section>
</div>
</body>
</html>
```